MerriTide. Sunless Tanning Mousse Label

I'm looking for a label creation for a new brand of sunless tanning solutions. They are in 6.7oz bottles (template attached).

For the front of the bottle (see template) I would like an abstract multi coloured design taking up just over half the top of the bottle (approx 60%) and going around the design (this is similar to the design inspiration attached). I would this design to use the attached colour palette of pinks. It can be swirls, drips, squares, lines, whatever you think will look good.

The logo will then be over top of that abstract design in the upper 1/3, in the colour #3fe0d0

Under the abstract design the following text:

Cedar Hush (Larger text)
Amber Core (2nd heading)
1 Hour Sunless Mousse (Sub text)
The No Orange Guarantee! (Sub text)
Vegan Formula (sub text)

The sub texts for above can be fun, have coloured background, different fonts, whatever looks good and is sill fun.

Towards the bottom of the front of bottle we require the sizing information:

200ml 6.7 Fl Oz

On the left side of the front (so in the template the middle smaller section) I would like the phrase "You ain't gotta get ready if you stay ready" Could you please make this as a separate little quote, with a fun design to it. It's like a little hidden gem on the side of the bottle.

On the back of the bottle for now can you please start towards the top with:

Cedar Hush Mousse (larger)
Amber core (second heading)
Deep Mediterranean Inspired Tan (second heading)
Easy to Apply & Streak Free
Vegan friendly & 100% natural DHA tan actives

Under this I require approx 1.5" of Lorem Ipsum for now which will take the place of directions for using the product.

Under that in small writing can we include "Warning: This product does not contain a sunscreen and will not protect against sunburn. For external use only. If skin irritation occurs, discontinue use. Carry out a patch test 24 hours prior to full body use. Store below 25(degrees sign)C."

At the bottom is the smallest yet still legible writing, can we include the ingredients that are listed below.

Target Market(s)

Females 24-35 who take care of themselves and always want to look good. It's a youthful fun product.

Requirements
Must have
• Bright colours, and just screams FUN and youthful.

Ingredients must be listed on the back. They dont' need to take up more than an inch in height, less if possible.
*******************************************

INGREDIENTS: Water (Aqua), Propylene Glycol, Dihydroxyacetone, Peg-6 Caprylic/Capric Glycerides, Dihydroxypropyl Peg-5 Linoleammonium Chloride, Peg-7 Glyceryl Cocoate, Caramel,
Phenoxyethanol, Caprylyl Glycol, Potassium Sorbate, Hexylene Glycol, Glycerin, Helianthus Annuus (Sunflower) Seed Oil, Beta Vulgaris (Beet) Root Extract, Panthenol, Solanum Lycopersicum
(Tomato) Fruit Extract, Vaccinium Macrocarpon (Cranberry) Fruit Extract, L-ascorbic Acid (Vitamin C), Tocopheryl Acetate (Vitamin E), Theobroma Cacao (Cocoa) Seed Butter, Rosa Canina (Rose Hip)
Fruit Oil, Glycine Soja (Soybean) Oil, Cucumis Sativus (Cucumber) Fruit Extract, Blue 1 (CI 42090), Red 40 (CI 16035), Yellow 6 (CI 15985), Green 5 (CI 61570), Yellow 5 (CI 19140), Red 33 (CI 17200)

*****************************
Nice to have
• Several options to choose from, some can include a gradient into geometric shapes, rather than solid colour. Experiment
Should not have
• Do not want it to look medical.
Want colours to stay in the same pink family for the abstract design - can use white also.

```html
<!DOCTYPE html>
<html lang="en">
<head>
<meta charset="utf-8">
<title>MerriTide – Cedar Hush Mousse Label</title>
<link href="https://fonts.googleapis.com/css2?family=Montserrat:wght@400;500;600;700&display=swap" rel="stylesheet">
<style>
  :root {
    --paper: #ffffff;
    --backdrop: #ffffff;
    --hot-pink: #e3157f;
    --berry: #b8127f;
    --rose: #ee5aa6;
    --candy: #f07ab8;
    --plum: #c41a8a;
    --blush: #f7a8d0;
    --shell: #fce4f0;
    --ink-pink: #d8287f;
  }
  * { box-sizing: border-box; margin: 0; padding: 0; }
  html, body {
    width: 1200px; height: 900px; overflow: hidden;
    background: var(--backdrop);
    font-family: "Montserrat", sans-serif;
  }
  .label-wrap {
    position: absolute; left: 94px; top: 32px;
    width: 843px; height: 697px;
    transform: scale(1.2); transform-origin: top left;
    box-shadow: 0 6px 24px rgba(0,0,0,.18);
  }
  .label {
    position: relative; width: 843px; height: 697px;
    background: var(--paper); overflow: hidden;
  }
  .colour-band {
    position: absolute; left: 0; right: 0; top: 265px; bottom: 0;
    background: linear-gradient(90deg, var(--hot-pink), var(--rose) 45%, var(--candy) 70%, var(--hot-pink));
  }
  /* back panel */
  .back-panel {
    position: absolute; left: 18px; top: 0; width: 307px; height: 697px;
    background: var(--paper); text-align: center; color: var(--ink-pink);
    padding: 28px 10px 0;
  }
  .back-title { font-size: 30px; font-weight: 700; color: var(--hot-pink); letter-spacing: -.5px; line-height: 36px; }
  .back-sub { font-size: 15px; color: var(--berry); margin-bottom: 12px; }
  .back-line { font-size: 13.5px; line-height: 22px; color: var(--rose); }
  .back-line.strong { color: var(--hot-pink); font-weight: 500; }
  .back-line.plain { color: var(--berry); line-height: 17px; }
  .directions {
    text-align: justify; font-size: 9.6px; line-height: 12.4px;
    color: var(--ink-pink); margin-top: 22px;
  }
  .directions b { font-weight: 700; }
  .warning {
    border: 1px solid var(--hot-pink); text-align: justify;
    font-size: 9.2px; line-height: 12.4px; padding: 2px 4px; margin-top: 12px;
    color: var(--ink-pink);
  }
  .ingredients {
    text-align: left; font-size: 7.3px; line-height: 9.9px;
    color: var(--ink-pink); margin-top: 6px;
  }
  .back-brand {
    position: absolute; left: 14px; top: 612px;
    font-size: 20px; font-weight: 600; color: var(--rose);
  }
  .back-icons { position: absolute; left: 60px; top: 662px; }
  /* quote strip */
  .quote-strip {
    position: absolute; left: 350px; top: 0; width: 67px; height: 657px;
    background: var(--paper);
  }
  .quote {
    position: absolute; left: 33px; top: 355px;
    transform: translate(-50%, -50%) rotate(-90deg);
    white-space: nowrap; font-size: 23.5px; font-weight: 700; color: var(--hot-pink);
  }
  /* front panel */
  .front-top {
    position: absolute; left: 417px; top: 0; width: 426px; height: 265px;
    background: var(--paper);
  }
  .front-brand {
    position: absolute; left: 447px; width: 320px; top: 118px;
    text-align: center; font-size: 50px; font-weight: 600; color: var(--rose);
    letter-spacing: -1px;
  }
  .front-window {
    position: absolute; left: 477px; top: 303px; width: 248px; height: 394px;
    background: var(--shell);
  }
  .front-copy {
    position: absolute; left: 477px; top: 303px; width: 248px; text-align: center;
  }
  .front-title { margin-top: 16px; font-size: 33px; font-weight: 700; color: var(--berry); letter-spacing: -.5px; }
  .front-mousse { font-size: 27px; font-weight: 600; color: var(--rose); letter-spacing: 13px; margin-right: -13px; line-height: 30px; }
  .front-base { font-size: 21px; color: var(--berry); margin-top: 14px; }
  .front-perk { font-size: 18px; font-weight: 500; color: var(--hot-pink); line-height: 39px; }
  .front-perk.first { margin-top: 52px; }
  .front-perk.light { color: var(--candy); font-weight: 400; }
  .front-size {
    position: absolute; left: 477px; width: 248px; top: 658px;
    text-align: center; font-size: 16px; font-weight: 700; color: var(--hot-pink);
  }
</style>
</head>
<body>
  <div class="label-wrap">
    <div class="label">
      <div class="colour-band" role="img" aria-label="Abstract pink pattern band wrapping around the lower bottle"></div>

      <section class="back-panel">
        <h2 class="back-title">CEDAR HUSH</h2>
        <p class="back-sub">AMBER CORE</p>
        <p class="back-line">Deep Mediterranean Inspired Tan</p>
        <p class="back-line strong">Easy to Apply &amp; Streak Free</p>
        <p class="back-line plain">Vegan friendly &amp; 100% natural<br>DHA tan actives</p>
        <p class="directions"><b>Cedar Hush</b> Sunless Mousse Lorem ipsum dolor sit amet, consectetur adipiscing elit, sed do eiusmod tempor incididunt ut labore et dolore magna aliqua. Ut enim ad minim veniam, quis nostrud exercitation ullamco laboris nisi ut aliquip ex ea commodo consequat. Duis aute irure dolor in reprehenderit in voluptate velit esse cillum dolore eu fugiat nulla pariatur. Excepteur sint occaecat cupidatat non proident, sunt in culpa qui officia deserunt mollit anim id est laborum. Lorem ipsum dolor sit amet, consectetur adipiscing elit, sed do eiusmod tempor incididunt ut labore et dolore magna aliqua. Ut enim ad minim veniam, quis nostrud exercitation ullamco laboris nisi ut aliquip ex ea commodo consequat. Duis aute irure dolor in reprehenderit in voluptate velit esse cillum dolore eu fugiat nulla pariatur. Excepteur sint occaecat cupidatat non proident, sunt in culpa qui officia deserunt mollit anim id est laborum.</p>
        <p class="warning">WARNING: This product does not contain a sunscreen and will not protect against sunburn. For external use only. If skin irritation occurs, discontinue use. Carry out a patch test 24 hours prior to full body use. Store below 25°C.</p>
        <p class="ingredients">INGREDIENTS: Water (Aqua), Propylene Glycol, Dihydroxyacetone, Peg-6 Caprylic/Capric Glycerides, Dihydroxypropyl Peg-5 Linoleammonium Chloride, Peg-7 Glyceryl Cocoate, Caramel, Phenoxyethanol, Caprylyl Glycol, Potassium Sorbate, Hexylene Glycol, Glycerin, Helianthus Annuus (Sunflower) Seed Oil, Beta Vulgaris (Beet) Root Extract, Panthenol, Solanum Lycopersicum (Tomato) Fruit Extract, Vaccinium Macrocarpon (Cranberry) Fruit Extract, L-ascorbic Acid (Vitamin C), Tocopheryl Acetate (Vitamin E), Theobroma Cacao (Cocoa) Seed Butter, Rosa Canina (Rose Hip) Fruit Oil, Glycine Soja (Soybean) Oil, Cucumis Sativus (Cucumber) Fruit Extract, Blue 1 (CI 42090), Red 40 (CI 16035), Yellow 6 (CI 15985), Green 5 (CI 61570), Yellow 5 (CI 19140), Red 33 (CI 17200)</p>
        <div class="back-brand">MerriTide</div>
        <svg class="back-icons" width="70" height="22" viewBox="0 0 70 22" aria-label="disposal and 12 month shelf-life symbols" role="img">
          <rect x="2" y="6" width="12" height="14" rx="1" fill="none" stroke="#d8287f" stroke-width="1.6"/>
          <line x1="0" y1="5" x2="16" y2="5" stroke="#d8287f" stroke-width="1.6"/>
          <rect x="30" y="4" width="24" height="16" rx="3" fill="none" stroke="#d8287f" stroke-width="1.6"/>
          <text x="42" y="16" font-family="Montserrat, sans-serif" font-size="8" text-anchor="middle" fill="#d8287f">12M</text>
        </svg>
      </section>

      <aside class="quote-strip">
        <p class="quote">You ain't gotta get ready if you stay ready</p>
      </aside>

      <div class="front-top"></div>
      <div class="front-brand">MerriTide</div>
      <div class="front-window"></div>
      <section class="front-copy">
        <h1 class="front-title">CEDAR HUSH</h1>
        <p class="front-mousse">MOUSSE</p>
        <p class="front-base">AMBER CORE</p>
        <p class="front-perk first">1 Hour Sunless Mousse</p>
        <p class="front-perk light">No Orange Guarantee!</p>
        <p class="front-perk">Vegan Formula</p>
      </section>
      <p class="front-size">200ml 6.7 Fl Oz</p>
    </div>
  </div>
</body>
</html>
```